Redfern Espresso Branding
Business Cards & Stationary Set
Professional
Dale Ostrander
Manager
1875 Heron Ridge Ave.
White Bear Lake, MN. 55110
r_fern@quillpost.net
I would like rounded corners on the business cards
Drive-thru to receive one free 12 oz. drink of choice!

```html
<!DOCTYPE html>
<html lang="en">
<head>
<meta charset="utf-8">
<title>Redfern Espresso Stationery</title>
<link href="https://fonts.googleapis.com/css2?family=Open+Sans:wght@400;600;700&display=swap" rel="stylesheet">
<style>
  :root {
    --backdrop: #ece8e1;
    --paper: #ffffff;
    --olive: #6b6a55;
    --olive-dark: #55543f;
    --rust: #c65a2b;
    --sand: #e3d6c2;
    --ink: #4a4a40;
    --rule: #c9c7bb;
  }
  * { box-sizing: border-box; margin: 0; padding: 0; }
  html, body { width: 1200px; height: 530px; overflow: hidden; }
  body { background: var(--backdrop); font-family: "Open Sans", Arial, sans-serif; color: var(--ink); position: relative; }
  .sheet { position: absolute; background: var(--paper); box-shadow: 0 2px 6px rgba(0,0,0,.18); overflow: hidden; }
  .letterhead { left: 30px; top: 22px; width: 360px; height: 490px; }
  .fax-sheet { left: 410px; top: 22px; width: 360px; height: 490px; }
  .brand { position: absolute; display: flex; align-items: center; gap: 5px; }
  .brand-mark { width: 14px; height: 14px; background: var(--olive); }
  .brand-name { font-weight: 700; font-size: 10px; color: var(--olive); white-space: nowrap; }
  .sheet .brand { left: 18px; top: 22px; }
  .contact { position: absolute; font-size: 6.5px; line-height: 1.55; color: var(--ink); }
  .sheet .contact { left: 190px; top: 12px; }
  .art { position: absolute; left: 120px; top: 320px; width: 150px; height: 125px; background: linear-gradient(180deg, #d8d6c8 0%, #b9b8a3 100%); opacity: .75; }
  .art-accent { position: absolute; left: 90px; top: 305px; width: 40px; height: 140px; background: #edc9b5; opacity: .7; }
  .swoosh { position: absolute; left: 0; bottom: 0; width: 100%; }
  .fax-bar { position: absolute; left: 0; top: 68px; width: 100%; height: 16px; background: var(--olive); }
  .fax-title { position: absolute; right: 18px; top: 66px; display: flex; align-items: center; gap: 4px; color: #fff; font-weight: 700; font-size: 11px; }
  .fax-form { position: absolute; left: 66px; top: 98px; width: 272px; height: 196px; border: 1px solid var(--rule); border-radius: 4px; padding: 8px 12px; }
  .field { display: flex; align-items: flex-end; gap: 6px; height: 16px; font-size: 6px; }
  .field span { width: 36px; text-align: right; }
  .field i { flex: 1; border-bottom: 1px dotted var(--rule); height: 1px; }
  .note-lines { margin-top: 6px; height: 42px; border-top: 1px solid var(--rule); background: repeating-linear-gradient(180deg, transparent 0 13px, #e4e2d9 13px 14px); }
  .tick-box { position: absolute; left: 20px; width: 22px; height: 10px; background: var(--olive); border-radius: 2px; }
  .card { position: absolute; width: 220px; height: 128px; border-radius: 10px; overflow: hidden; box-shadow: 0 2px 5px rgba(0,0,0,.2); }
  .card-front { left: 800px; top: 40px; background: var(--paper); }
  .card-back { left: 960px; top: 185px; background: var(--olive); }
  .card-front .brand { left: 14px; top: 22px; }
  .card-person { position: absolute; right: 14px; top: 40px; text-align: right; font-size: 7px; line-height: 1.5; }
  .card-person strong { font-size: 8.5px; color: var(--olive-dark); }
  .card-curve { position: absolute; left: 0; bottom: 16px; width: 100%; }
  .card-offer { position: absolute; left: 0; right: 0; bottom: 6px; text-align: center; font-size: 6px; color: var(--rust); font-weight: 600; }
  .card-back .brand { left: 50%; top: 50%; transform: translate(-50%, -50%); }
  .card-back .brand-mark { background: #fff; }
  .card-back .brand-name { color: #fff; font-size: 12px; }
  .envelope { left: 800px; top: 335px; width: 380px; height: 170px; }
  .envelope .brand { left: 16px; top: 86px; }
  .envelope .contact { left: 16px; top: 108px; }
</style>
</head>
<body>

<section class="sheet letterhead">
  <div class="brand"><span class="brand-mark"></span><span class="brand-name">Redfern Espresso</span></div>
  <div class="contact">1875 Heron Ridge Ave.<br>White Bear Lake, MN. 55110<br>p. (555) 014-2290<br>e. r_fern@quillpost.net</div>
  <div class="art-accent"></div>
  <div class="art" role="img" aria-label="Faint pine tree illustration"></div>
  <svg class="swoosh" viewBox="0 0 360 70" height="70" preserveAspectRatio="none">
    <path d="M0 40 Q180 5 360 30 L360 70 L0 70Z" fill="var(--olive)"/>
    <path d="M0 34 Q180 0 360 22 L360 27 Q180 7 0 40Z" fill="var(--rust)"/>
  </svg>
</section>

<section class="sheet fax-sheet">
  <div class="brand"><span class="brand-mark"></span><span class="brand-name">Redfern Espresso</span></div>
  <div class="contact">1875 Heron Ridge Ave.<br>White Bear Lake, MN. 55110<br>p. (555) 014-2290<br>e. r_fern@quillpost.net</div>
  <div class="fax-bar"></div>
  <div class="fax-title">
    <svg width="14" height="8" viewBox="0 0 14 8"><path d="M0 4H11M8 1L12 4L8 7" stroke="#fff" stroke-width="1.4" fill="none"/></svg>
    FAX
  </div>
  <div class="tick-box" style="top:118px"></div>
  <div class="tick-box" style="top:200px"></div>
  <div class="fax-form">
    <div class="field"><span>To</span><i></i></div>
    <div class="field"><span>Company</span><i></i></div>
    <div class="field"><span>Fax</span><i></i></div>
    <div class="field"><span>Phone</span><i></i></div>
    <div class="field"><span>From</span><i></i></div>
    <div class="field"><span>Date</span><i></i></div>
    <div class="field"><span>Pages</span><i></i></div>
    <div class="field"><span>Re</span><i></i></div>
    <div class="note-lines"></div>
  </div>
  <div class="art-accent"></div>
  <div class="art" role="img" aria-label="Faint pine tree illustration"></div>
  <svg class="swoosh" viewBox="0 0 360 70" height="70" preserveAspectRatio="none">
    <path d="M0 40 Q180 5 360 30 L360 70 L0 70Z" fill="var(--olive)"/>
    <path d="M0 34 Q180 0 360 22 L360 27 Q180 7 0 40Z" fill="var(--rust)"/>
  </svg>
</section>

<section class="card card-front">
  <div class="brand"><span class="brand-mark"></span><span class="brand-name">Redfern Espresso</span></div>
  <div class="card-person"><strong>Dale Ostrander</strong><br>Manager<br>1875 Heron Ridge Ave.<br>White Bear Lake, MN. 55110<br>r_fern@quillpost.net</div>
  <svg class="card-curve" viewBox="0 0 220 20" height="20" preserveAspectRatio="none">
    <path d="M0 14 Q110 0 220 8 L220 11 Q110 4 0 17Z" fill="var(--rust)"/>
  </svg>
  <div class="card-offer">Drive-thru to receive one free 12 oz. drink of choice!</div>
</section>

<section class="card card-back">
  <div class="brand"><span class="brand-mark"></span><span class="brand-name">Redfern Espresso</span></div>
</section>

<section class="sheet envelope">
  <svg class="swoosh" viewBox="0 0 380 60" height="60" preserveAspectRatio="none" style="top:0;bottom:auto">
    <path d="M0 0 H380 V30 Q190 60 0 30Z" fill="var(--olive)"/>
    <path d="M0 32 Q190 62 380 32 L380 36 Q190 66 0 36Z" fill="var(--rust)"/>
  </svg>
  <div class="brand"><span class="brand-mark"></span><span class="brand-name">Redfern Espresso</span></div>
  <div class="contact">1875 Heron Ridge Ave.<br>White Bear Lake, MN. 55110</div>
</section>

</body>
</html>
```